Security Company Needs a Website *

We need a website that gives our clients information about the services we provide, methods of contacting us and landing page to advertise on social media sites.

We need five landing pages titled Home, About Us, Services, Contact Us and a Landing Page that can be linked to Chatterlane advertising.

About Us - Should have a section for Core Values & Ethics, Our Vision, Our Mission and Partners.

Services - This page should show the different categories which include CCTV, Security Alarms, Access Control and Fire Protection.

CCTV Service Description:
Closed circuit television (CCTV) has long been implemented by businesses as a surveillance tool in areas that need monitoring. With digital CCTV cameras, multiple video cameras transmit signals through a set of monitors. The cameras provide thorough surveillance of the area.

With vast technological improvements over the last ten years, businesses with CCTV systems can use unique IP cameras and video analytics to monitor traffic flows, people-count, implement facial and number plate recognition. Useful information about customer behaviour and demographics can be discovered too. CCTV helps prevent crime in many industries and can assist with the improvement of industrial processes, safety on transport systems and traffic monitoring.

Security Alarms Service Description:
Alarms systems are electronic devices programmed to alert people to specific dangers and detect intrusions, fire or theft. Security alarms, systems and access control monitoring combine to create an integrated surveillance solution, tailored to your business’ unique requirements. Our surveillance and alarm monitoring services are ideal for perimeter protection from unwanted intruders or potential dangers.

Access Control Services:
An access control system allows for the free flow of authorised personnel while denying entry to unwanted visitors. With walk-in thieves and trespassers shut out, you dramatically reduce your exposure to crime while increasing the security of your employees, visitors, information and assets.

* Control when and who is entering your premises
* Protect employees, assets and information
* Secure an area or sector
* Observe movement
* Integrate with other security systems

Our range of access control systems can be seamlessly linked to other systems in our portfolio. These include Fire Detection Systems, Intruder Alarms, CCTV, and Building Management. A common request involves the need for a CCTV camera to pan around and focus on a door that has been highlighted as a security risk by the access control system.

Fire Protection Service:
To Be Advised

The above copy-writing will also have to be changed.

Contact Us - This form needs to be simple and straightforward to gather the prospects information and we would like to have a call to action on this page. The Contact Us page should also have a wayfindr plot location of our office address.

We would also like to have a link to our chatterlane page on the website.

Target Market(s)

Commercial businesses, building construction developers and property managers.

Industry/Entity Type

Security

Number of Pages Required

5+ page

Font styles to use
Sans Serif

Colors

Designer to choose colors to be used in the design.

Requirements
Must have
• We need to have the same look and feel as well as website features as the following website:
• https://www.kovrangard.com.au/business-security/
• The website must be easy to use and easy to edit as well.

```html
<!DOCTYPE html>
<html lang="en">
<head>
<meta charset="utf-8">
<title>Wardline Security</title>
<link href="https://fonts.googleapis.com/css2?family=Poppins:wght@300;400;500;600;700&display=swap" rel="stylesheet">
<style>
:root{
  --navy:#1e4f91;
  --nav:#1668b8;
  --nav-active:#2c56a3;
  --hero-a:#3a2c8c;
  --hero-b:#2c5ab4;
  --ink:#221a66;
  --grey:#8a8a8a;
  --dark:#0a0a0d;
  --white:#fff;
  --link:#2f7fe0;
}
*{box-sizing:border-box;margin:0;padding:0}
html,body{width:1200px;height:1200px;overflow:hidden}
body{position:relative;font-family:'Poppins',sans-serif;background:var(--white);color:#222}
.abs{position:absolute}
.brand{left:217px;top:26px;display:flex;align-items:center;gap:9px;color:#1d2a5a;font-size:18px;font-weight:500;line-height:1}
.brand-mark{width:12px;height:12px;background:#1d2a5a}
.call{left:894px;top:12px;color:var(--navy);font-weight:600;font-size:17px;line-height:22px}
.nav{left:0;top:64px;width:1200px;height:37px;background:var(--nav)}
.nav-item{position:absolute;top:0;height:37px;line-height:37px;color:var(--white);font-size:14px;text-align:center;border-right:1px solid rgba(0,0,0,.12)}
.nav-item.active{background:var(--nav-active)}
.search{position:absolute;left:838px;top:0;width:207px;height:37px;border-left:1px solid rgba(0,0,0,.12);border-right:1px solid rgba(0,0,0,.12);color:rgba(255,255,255,.75);font-size:12px;line-height:37px;padding-left:16px}
.search svg{position:absolute;right:12px;top:11px}
.hero{left:0;top:101px;width:1200px;height:308px;background:linear-gradient(100deg,var(--hero-a) 0%,#33419e 45%,var(--hero-b) 100%)}
.hero-photo{position:absolute;left:620px;top:0;width:580px;height:308px;background:linear-gradient(90deg,rgba(60,70,170,0) 0%,rgba(90,110,200,.35) 50%,rgba(70,100,190,.25) 100%)}
.hero-title{left:153px;top:189px;color:var(--white);font-size:27px;font-weight:700}
.hero-text{left:153px;top:234px;width:560px;color:var(--white);font-size:15.5px;font-weight:300;line-height:21px}
.hero-btn{left:154px;top:297px;width:101px;height:32px;border-radius:16px;background:var(--white);color:#24237a;font-size:13px;font-weight:600;text-align:center;line-height:32px;box-shadow:0 3px 0 rgba(0,0,0,.15)}
.dot{top:359px;width:8px;height:8px;border-radius:50%;border:2px solid var(--white)}
.quote{left:786px;top:166px;width:259px;height:243px;border-radius:24px 24px 0 0;background:rgba(35,60,150,.75)}
.quote h3{position:absolute;top:21px;width:100%;text-align:center;color:var(--white);font-size:19px;font-weight:700}
.quote .rule{position:absolute;left:40px;top:53px;width:180px;height:1px;background:rgba(255,255,255,.25)}
.q-field{position:absolute;left:32px;width:195px;height:26px;background:var(--white);color:#999;font-size:11px;line-height:26px;padding-left:9px}
.q-field svg{position:absolute;right:10px;top:10px}
.q-submit{position:absolute;right:32px;top:212px;color:var(--white);font-size:11px;font-weight:600}
.mission-title{left:0;top:440px;width:1200px;text-align:center;color:var(--ink);font-size:23px;font-weight:700}
.mission-rule{left:579px;top:479px;width:42px;height:1px;background:#222}
.mission-text{left:240px;top:499px;width:720px;text-align:center;color:var(--grey);font-size:13.5px;font-weight:300;line-height:21px}
.card-img{top:572px;width:277px;height:192px}
.card-cap{top:785px;width:277px;text-align:center;font-size:14px;color:#1a1a1a}
.arrow{top:661px;width:21px;height:21px;border-radius:50%;background:#e6e6e6}
.footer{left:0;top:832px;width:1200px;height:368px;background:linear-gradient(120deg,#161619 0%,var(--dark) 55%,#141417 100%)}
.f-title{left:153px;top:853px;color:var(--white);font-size:23px;font-weight:700}
.f-title-rule{left:153px;top:884px;width:48px;height:1px;background:#888}
.f-field{border:1px solid #5a5a5a;color:#777;font-size:12px;font-weight:300;padding:6px 9px}
.send{left:153px;top:1118px;color:var(--white);font-size:13.5px;font-weight:500}
.f-head{top:908px;color:var(--white);font-size:18px;font-weight:500}
.info-label{left:672px;color:#e6e6e6;font-size:12px}
.info-val{left:672px;color:#8a8a8a;font-size:12px;font-weight:300}
.info-icon{left:647px}
.ql{left:904px;color:#777;font-size:12px;font-weight:300}
.bottom-rule{left:153px;top:1164px;width:892px;height:1px;background:#333}
.copy{left:153px;top:1173px;color:#eee;font-size:12px}
.copy span{color:var(--link)}
.social{right:155px;top:1176px;display:flex;gap:12px;color:#ddd;font-size:10px;font-weight:500}
</style>
</head>
<body>

<header>
  <div class="abs brand"><span class="brand-mark"></span>WARDLINE SECURITY</div>
  <div class="abs call">Call Us Now<br>(080) 41720 38815</div>
</header>

<nav class="abs nav">
  <div class="nav-item active" style="left:154px;width:81px">Home</div>
  <div class="nav-item" style="left:235px;width:101px">About Us</div>
  <div class="nav-item" style="left:336px;width:97px">Services</div>
  <div class="nav-item" style="left:433px;width:120px">Contact&nbsp; Us</div>
  <div class="search">Search
    <svg width="14" height="14" viewBox="0 0 14 14"><circle cx="6" cy="6" r="4.5" fill="none" stroke="rgba(255,255,255,.75)" stroke-width="1.8"/><line x1="9.3" y1="9.3" x2="13" y2="13" stroke="rgba(255,255,255,.75)" stroke-width="2"/></svg>
  </div>
</nav>

<section class="abs hero">
  <div class="hero-photo" role="img" aria-label="Blue-tinted security camera mounted on a wall"></div>
</section>
<h1 class="abs hero-title">Access Control Services</h1>
<p class="abs hero-text">An access control system allows for the free flow of authorised personnel while denying entry to unwanted visitors</p>
<div class="abs hero-btn">MORE INFO</div>
<div class="abs dot" style="left:157px"></div>
<div class="abs dot" style="left:175px"></div>
<div class="abs dot" style="left:197px;border-color:rgba(255,255,255,.5)"></div>

<form class="abs quote">
  <h3>Request A Quote</h3>
  <div class="rule"></div>
  <div class="q-field" style="top:77px">Name</div>
  <div class="q-field" style="top:111px">Email</div>
  <div class="q-field" style="top:144px">Contact Number</div>
  <div class="q-field" style="top:175px">Service
    <svg width="9" height="6" viewBox="0 0 9 6"><polyline points="1,1 4.5,4.5 8,1" fill="none" stroke="#666" stroke-width="1.2"/></svg>
  </div>
  <div class="q-submit">SUBMIT</div>
</form>

<section>
  <h2 class="abs mission-title">Our Mission</h2>
  <div class="abs mission-rule"></div>
  <p class="abs mission-text">Lorem ipsum dolor sit amet, consectetur adipiscing elit, sed do eiusmod tempor incididunt ut labore et dolore magna aliqua. Ut enim ad minim veniam, quis nostrud exercitation ullamco laboris</p>

  <div class="abs arrow" style="left:119px"><svg width="21" height="21" viewBox="0 0 21 21"><polyline points="12,6 8,10.5 12,15" fill="none" stroke="#fff" stroke-width="1.8"/></svg></div>
  <div class="abs arrow" style="left:1061px"><svg width="21" height="21" viewBox="0 0 21 21"><polyline points="9,6 13,10.5 9,15" fill="none" stroke="#fff" stroke-width="1.8"/></svg></div>

  <div class="abs card-img" style="left:153px;background:linear-gradient(180deg,#4b8fc4 0%,#6aa7d6 55%,#3f7a5a 100%)" role="img" aria-label="Dome CCTV camera on a pole against a glass building"></div>
  <div class="abs card-cap" style="left:153px">CCTV SECURITY SYSTEM</div>
  <div class="abs card-img" style="left:462px;background:linear-gradient(90deg,#e9e9e9 0%,#ddd 35%,#d8343a 45%,#d8343a 62%,#e4e4e4 72%,#ececec 100%)" role="img" aria-label="Red fire alarm pull station on a white wall"></div>
  <div class="abs card-cap" style="left:462px">SECURITY ALARMS</div>
  <div class="abs card-img" style="left:770px;background:linear-gradient(135deg,#2d2d2f 0%,#bfc2c6 40%,#a9adb2 60%,#2a2a2c 100%)" role="img" aria-label="Hand holding a key fob to an access control keypad"></div>
  <div class="abs card-cap" style="left:770px">ACCESS CONTROL SYSTEM</div>
</section>

<footer class="abs footer"></footer>
<h2 class="abs f-title">Contact Us</h2>
<div class="abs f-title-rule"></div>
<div class="abs f-field" style="left:152px;top:914px;width:217px;height:27px">Name</div>
<div class="abs f-field" style="left:389px;top:914px;width:218px;height:27px">Email</div>
<div class="abs f-field" style="left:152px;top:959px;width:217px;height:27px">Phone</div>
<div class="abs f-field" style="left:389px;top:959px;width:218px;height:27px">Company</div>
<div class="abs f-field" style="left:152px;top:1005px;width:455px;height:103px">Message</div>
<div class="abs send"><span style="margin-right:10px">&rarr;</span> Send Now</div>

<h3 class="abs f-head" style="left:647px">Get in Touch</h3>
<svg class="abs info-icon" style="top:948px" width="13" height="12" viewBox="0 0 13 12"><path d="M6.5 0 L13 6 H11 V12 H8 V8 H5 V12 H2 V6 H0 Z" fill="#ddd"/></svg>
<div class="abs info-label" style="top:946px">Office Address</div>
<div class="abs info-val" style="top:973px">48 Harlow Lane, Brookmere, UK</div>
<svg class="abs info-icon" style="top:1008px" width="14" height="11" viewBox="0 0 14 11"><rect x=".7" y=".7" width="12.6" height="9.6" fill="none" stroke="#ddd" stroke-width="1.2"/><polyline points="1,1 7,6 13,1" fill="none" stroke="#ddd" stroke-width="1.2"/></svg>
<div class="abs info-label" style="top:1005px">Email</div>
<div class="abs info-val" style="top:1028px">hello@wardline-mail.com</div>
<svg class="abs info-icon" style="top:1060px" width="12" height="12" viewBox="0 0 12 12"><path d="M2 0 L4.5 2.5 L3 4.5 Q4.5 7.5 7.5 9 L9.5 7.5 L12 10 L10 12 Q1 10 0 2 Z" fill="#ddd"/></svg>
<div class="abs info-label" style="top:1057px">Phone</div>
<div class="abs info-val" style="top:1081px">(080) 41720 38890</div>

<h3 class="abs f-head" style="left:902px">Quick links</h3>
<div class="abs ql" style="top:948px">Home</div>
<div class="abs ql" style="top:974px">About Us</div>
<div class="abs ql" style="top:1000px">Services</div>
<div class="abs ql" style="top:1027px">FAQ</div>
<div class="abs ql" style="top:1053px">Customer Support</div>
<div class="abs ql" style="top:1079px">Privacy Polacy</div>

<div class="abs bottom-rule"></div>
<div class="abs copy">© Copyright 2018 - <span>Wardline Security</span> - All right reserved.</div>
<div class="abs social"><span>Chatterlane</span><span>Chirpline</span><span>Linkwork</span><span>Orbitplus</span></div>

</body>
</html>
```